Business Card Design Project

I have established a company called "Morrowvale" which is a business specialising in psychotherapy/counselling , predominantly for anxiety & depression.

My name is Tev....hence, the Morrowvale link. However, Morrowvale was also chosen for its reference to green shoots of growth/recovery.

Morrowvale is to be "upmarket" and highly professional. I'm keen for the style and colours to reflect this.....taupe/grey with navy/black script, for example.....NO primary colours.

My name needs to be on the card and my mobile number. Not sure, but suspect it should also have my qualifications ( BA (Psych) & BSc (Hons) Psychology). Mobile number 0491 627 850.

```html
<!DOCTYPE html>
<html lang="en">
<head>
<meta charset="utf-8">
<title>Morrowvale business card options</title>
<link rel="stylesheet" href="https://fonts.googleapis.com/css2?family=Quicksand:wght@400;500&family=Open+Sans:wght@300;400&family=Michroma&display=swap">
<style>
  :root {
    --plum: #35214f;
    --slate: #5e6266;
    --leaf: #76b43a;
    --white: #ffffff;
    --taupe-light: #8f887c;
    --taupe-dark: #675e52;
    --ink: #2a2a2a;
  }
  html, body {
    margin: 0;
    padding: 0;
    width: 1012px;
    height: 1200px;
    overflow: hidden;
    background: var(--white);
  }
  .sheet {
    position: relative;
    width: 1012px;
    height: 1200px;
  }
  .column-label {
    position: absolute;
    top: 12px;
    margin: 0;
    font-family: "Quicksand", sans-serif;
    font-weight: 500;
    font-size: 18px;
    color: var(--plum);
  }
  .column-label--front { left: 25px; }
  .column-label--back { left: 514px; }
  .card {
    position: absolute;
    width: 474px;
    height: 263px;
    box-sizing: border-box;
    border: 1px solid var(--ink);
    overflow: hidden;
  }
  .card--front { left: 25px; }
  .card--back { left: 514px; }
  .row-1 { top: 39px; }
  .row-2 { top: 328px; }
  .row-3 { top: 617px; }
  .row-4 { top: 906px; }

  .bg-plum { background: var(--plum); }
  .bg-slate { background: var(--slate); }
  .bg-leaf { background: var(--leaf); }
  .bg-white { background: var(--white); }
  .bg-taupe {
    background: radial-gradient(ellipse at 45% 40%, var(--taupe-light) 0%, #807869 55%, var(--taupe-dark) 100%);
  }

  .wordmark {
    position: absolute;
    margin: 0;
    font-family: "Quicksand", sans-serif;
    font-weight: 400;
    font-size: 62px;
    letter-spacing: 1px;
    line-height: 1;
  }
  .wordmark--right { right: 26px; bottom: 22px; }
  .wordmark--left { left: 86px; bottom: 22px; }
  .wordmark--white { color: var(--white); }
  .wordmark--plum { color: var(--plum); }

  .mark-dot {
    position: absolute;
    width: 16px;
    height: 16px;
    border-radius: 50%;
  }
  .mark-dot--white { background: var(--white); }
  .mark-dot--plum { background: var(--plum); }
  .mark-dot--leaf { background: var(--leaf); }

  .contact-centered {
    position: absolute;
    left: 0;
    right: 0;
    top: 98px;
    text-align: center;
    font-family: "Open Sans", sans-serif;
  }
  .contact-centered .name {
    margin: 0;
    font-weight: 300;
    font-size: 21px;
    line-height: 1.2;
  }
  .contact-centered .qualifications {
    margin: 2px 0 0;
    font-weight: 400;
    font-size: 8px;
  }
  .contact-centered .phone {
    margin: 6px 0 0;
    font-weight: 400;
    font-size: 18px;
  }
  .text-plum { color: var(--plum); }
  .text-white { color: var(--white); }

  .contact-tech {
    position: absolute;
    font-family: "Michroma", sans-serif;
    color: var(--slate);
    text-transform: lowercase;
  }
  .contact-tech--right {
    right: 30px;
    top: 34px;
    text-align: right;
  }
  .contact-tech--right .name { margin: 0; font-size: 15px; }
  .contact-tech--right .qualifications { margin: 2px 0 0; font-size: 7px; line-height: 1.4; }
  .contact-tech--right .phone { margin: 20px 0 0; font-size: 12px; }

  .contact-tech--bottom {
    left: 22px;
    bottom: 22px;
    color: var(--white);
  }
  .contact-tech--bottom .name { margin: 0; font-size: 12px; }
  .contact-tech--bottom .qualifications { margin: 6px 0 0; font-size: 7px; }
</style>
</head>
<body>
<main class="sheet">
  <h2 class="column-label column-label--front">front options</h2>
  <h2 class="column-label column-label--back">back options</h2>

  <section class="card card--front row-1 bg-plum">
    <span class="mark-dot mark-dot--white" style="right:130px; bottom:98px;"></span>
    <p class="wordmark wordmark--right wordmark--white">morrowvale</p>
  </section>
  <section class="card card--back row-1 bg-white">
    <div class="contact-centered text-plum">
      <p class="name">Tev Marlow</p>
      <p class="qualifications">BA (Psych) &amp; BSc (Hons) Psychology</p>
      <p class="phone">0491 627 850</p>
    </div>
  </section>

  <section class="card card--front row-2 bg-taupe" role="img" aria-label="Textured taupe background with the Morrowvale name">
    <span class="mark-dot mark-dot--plum" style="left:284px; bottom:98px;"></span>
    <p class="wordmark wordmark--left wordmark--plum">morrowvale</p>
  </section>
  <section class="card card--back row-2 bg-plum">
    <div class="contact-centered text-white">
      <p class="name">Tev Marlow</p>
      <p class="qualifications">BA (Psych) &amp; BSc (Hons) Psychology</p>
      <p class="phone">0491 627 850</p>
    </div>
  </section>

  <section class="card card--front row-3 bg-slate">
    <span class="mark-dot mark-dot--leaf" style="right:130px; bottom:98px;"></span>
    <p class="wordmark wordmark--right wordmark--white">morrowvale</p>
  </section>
  <section class="card card--back row-3 bg-leaf">
    <div class="contact-tech contact-tech--right">
      <p class="name">Tev Marlow</p>
      <p class="qualifications">BA (Psych) &amp;<br>BSc (Hons) Psychology</p>
      <p class="phone">0491 627 850</p>
    </div>
  </section>

  <section class="card card--front row-4 bg-taupe" role="img" aria-label="Textured taupe background with the Morrowvale name">
    <span class="mark-dot mark-dot--white" style="left:284px; bottom:98px;"></span>
    <p class="wordmark wordmark--left wordmark--white">morrowvale</p>
  </section>
  <section class="card card--back row-4 bg-slate">
    <div class="contact-tech contact-tech--bottom">
      <p class="name">Tev Marlow - 0491 627 850</p>
      <p class="qualifications">BA (Psych) and BSc (Hons) Psychology</p>
    </div>
  </section>
</main>
</body>
</html>
```